New business card/stationary for a consulting company

I am looking for a clean and very professional looking business card for my consulting company as well as corresponding stationary. I am uploading our logo. I like simple and powerful for the feel. No graphics but I am open on everything else. Below is my contact information but would like the final to be in a version I can add my employees information into and print. Thank you.

Daniel Whitcombe
dan@fernlowadvisory.com
2837 North 9th Avenue, Summit Floor, Alder Ridge, Ohio 60483
www.fernlowadvisory.com

Industry/Entity Type

Consulting

Contact Information for Business Card

Daniel Whitcombe
dan@fernlowadvisory.com
www.fernlowadvisory.com

Font styles to use
Serif
Sans Serif

Requirements
Must have
• Our logo and the business card details.
Nice to have
• our website www.fernlowadvisory.com

```html
<!DOCTYPE html>
<html lang="en">
<head>
<meta charset="utf-8">
<title>Fernlow Advisory — Business Card</title>
<link rel="stylesheet" href="https://fonts.googleapis.com/css2?family=Tenor+Sans&display=swap">
<style>
  :root {
    --navy: #23236b;
    --paper: #ffffff;
    --backdrop: #3b3b3d;
    --font-main: "Tenor Sans", sans-serif;
  }
  * { margin: 0; padding: 0; box-sizing: border-box; }
  html, body {
    width: 1200px; height: 900px; overflow: hidden;
    background: var(--backdrop);
    font-family: var(--font-main);
    color: var(--navy);
  }
  .card {
    position: absolute;
    left: 270px;
    width: 660px; height: 377px;
    background: var(--paper);
    border-radius: 16px;
    overflow: hidden;
  }
  .card--back { top: 48px; }
  .card--front { top: 475px; }

  /* back side */
  .back-mark {
    position: absolute; left: 0; right: 0; top: 110px;
    text-align: center;
  }
  .brand-square {
    display: block; margin: 0 auto 6px;
    width: 120px; height: 60px; background: var(--navy);
    border-bottom: 4px solid var(--paper);
    box-shadow: 0 4px 0 var(--navy);
  }
  .brand-name {
    font-size: 38px; letter-spacing: 2px; text-transform: uppercase;
    margin-top: 8px; line-height: 1;
  }
  .back-web {
    position: absolute; left: 0; right: 0; top: 250px;
    text-align: center; font-size: 12px; letter-spacing: 1px; text-transform: uppercase;
  }

  /* front side */
  .name-band {
    position: absolute; left: 0; top: 34px; width: 430px; height: 34px;
    background: var(--navy); color: var(--paper);
    font-size: 17px; letter-spacing: 1.5px; text-transform: uppercase;
    padding: 6px 0 0 40px;
  }
  .band-rule {
    position: absolute; height: 2px; background: var(--navy);
  }
  .front-square {
    position: absolute; left: 440px; top: 34px; width: 110px; height: 64px;
    background: var(--navy);
  }
  .right-band {
    position: absolute; left: 560px; top: 58px; width: 100px; height: 40px;
    background: var(--navy);
  }
  .front-brand {
    position: absolute; right: 36px; top: 112px;
    font-size: 34px; letter-spacing: 2px; text-transform: uppercase; line-height: 1;
  }
  .divider {
    position: absolute; left: 40px; top: 160px; width: 580px; height: 1px; background: var(--navy);
  }
  .contacts {
    position: absolute; left: 40px; top: 178px; list-style: none;
    font-size: 14px; letter-spacing: 1px; text-transform: uppercase;
  }
  .contacts li { display: flex; align-items: center; gap: 10px; height: 24px; }
  .contacts svg { width: 15px; height: 15px; fill: var(--navy); flex: none; }
  .address {
    position: absolute; right: 40px; top: 196px; text-align: right;
    font-size: 17px; letter-spacing: 1.5px; font-variant: small-caps; line-height: 1.35;
    font-style: normal;
  }
  .bottom-band {
    position: absolute; left: 0; right: 0; bottom: 0; height: 26px; background: var(--navy);
  }
</style>
</head>
<body>

<section class="card card--back" aria-label="Card back">
  <div class="back-mark">
    <span class="brand-square"></span>
    <p class="brand-name">Fernlow Advisory</p>
  </div>
  <p class="back-web">www.fernlowadvisory.com</p>
</section>

<section class="card card--front" aria-label="Card front">
  <div class="name-band">Daniel Whitcombe</div>
  <div class="band-rule" style="left:0; top:72px; width:430px;"></div>
  <div class="front-square"></div>
  <div class="band-rule" style="left:440px; top:102px; width:110px;"></div>
  <div class="right-band"></div>
  <div class="band-rule" style="left:560px; top:102px; width:100px;"></div>

  <p class="front-brand">Fernlow Advisory</p>
  <div class="divider"></div>

  <ul class="contacts">
    <li>
      <svg viewBox="0 0 16 16" aria-hidden="true"><path d="M3 1h3l1.5 4-2 1.2a8 8 0 0 0 4.3 4.3L11 8.5l4 1.5v3a2 2 0 0 1-2 2A13 13 0 0 1 1 3a2 2 0 0 1 2-2z"/></svg>
      5820-4182-0365
    </li>
    <li>
      <svg viewBox="0 0 16 16" aria-hidden="true"><path d="M1 3h14v10H1z M1.8 3.8 8 9l6.2-5.2" stroke="#fff" stroke-width="1.2"/></svg>
      dan@fernlowadvisory.com
    </li>
    <li>
      <svg viewBox="0 0 16 16" aria-hidden="true"><circle cx="8" cy="8" r="7"/><path d="M1 8h14M8 1c-3 3.5-3 10.5 0 14M8 1c3 3.5 3 10.5 0 14" stroke="#fff" stroke-width="1" fill="none"/></svg>
      www.fernlowadvisory.com
    </li>
  </ul>

  <address class="address">
    2837 North 9th Avenue<br>
    Summit Floor, Alder Ridge<br>
    Ohio 60483
  </address>

  <div class="band-rule" style="left:0; right:0; bottom:34px;"></div>
  <div class="bottom-band"></div>
</section>

</body>
</html>
```